Make my Savory Fungi Strips sell!!

Design for a new mushroom jerky product.
The meatiest (no) beef jerky ever!!
Bite it! Rip it! Tear it! Chew it! There is nothing meatier! Not even meat!
Please use our company logo (supplied) somewhere on the package. It does not have to be the focus. Just anywhere in the design.
Not sure if I want to focus on the plant based, healthy, clean - eating design or a masculine, taste based, BBQ, design. Surprise me!
Will be used on a stand up pouch, with a window.

Target Market(s)

Jerky lovers. Plant based connoisseurs. Vegans. Millenials. People that want a true meat experience without the cruelty.

Requirements
Must have
• Verdant Crest Foods logo.
Nice to have
• Mushrooms, shiitake, nature, muscles, happy cows?,
Should not have
• The word vegan. Stick to Plant Based.

```html
<!DOCTYPE html>
<html lang="en">
<head>
<meta charset="utf-8">
<title>Mushroom Jerky Pouch</title>
<link rel="stylesheet" href="https://fonts.googleapis.com/css2?family=Oswald:wght@700&family=Baloo+2:wght@800&family=Montserrat:wght@800;900&display=swap">
<style>
  :root {
    --bg: #2a9ea3;
    --orange-light: #ffb21a;
    --orange: #ff9a12;
    --ink: #0d0d0d;
    --white: #ffffff;
    --silver: #e4e4e4;
    --blue: #1450a8;
    --blue-light: #1d63c4;
    --gold-text: #f6e7b8;
    --photo-dark: #3a1c12;
    --photo-mid: #7a3a22;
    --leaf-green: #8cc63f;
  }
  * { box-sizing: border-box; margin: 0; padding: 0; }
  html, body { width: 1200px; height: 1020px; overflow: hidden; }
  body { background: var(--bg); position: relative; }

  .pouch {
    position: absolute; left: 330px; top: 110px;
    width: 540px; height: 800px;
    border-radius: 16px;
    background: linear-gradient(180deg, var(--orange) 0%, var(--orange-light) 45%, var(--orange) 100%);
    overflow: hidden;
  }
  .pouch-art { position: absolute; inset: 0; width: 540px; height: 800px; }

  .plant-badge {
    position: absolute; left: 70px; top: 112px;
    display: flex; flex-direction: column; align-items: center; gap: 6px;
    color: var(--white); font: 800 12px "Montserrat", sans-serif;
  }
  .plant-badge .dot { width: 24px; height: 24px; border-radius: 50%; background: var(--white); }

  .product-title {
    position: absolute; left: 80px; top: 158px; width: 380px;
    color: var(--white); font-family: "Oswald", sans-serif; font-weight: 700;
    text-align: center; transform: rotate(-8deg); line-height: 1;
  }
  .product-title .line-1 { display: block; font-size: 78px; letter-spacing: -1px; }
  .product-title .line-2 { display: block; font-size: 84px; margin-top: -2px; letter-spacing: -1px; }

  .brand-tag {
    position: absolute; left: 356px; top: 330px; width: 112px; height: 108px;
    background: var(--white);
    display: flex; flex-direction: column; align-items: center; justify-content: center; gap: 10px;
    transform: rotate(-4deg);
  }
  .brand-tag .mark { width: 34px; height: 34px; border-radius: 50%; background: var(--leaf-green); }
  .brand-tag .name {
    font: 800 10px "Montserrat", sans-serif; color: var(--ink);
    text-align: center; line-height: 1.2; text-transform: uppercase;
  }

  .chant {
    position: absolute; left: 42px; top: 398px; width: 150px; height: 168px;
    background: linear-gradient(160deg, var(--blue-light), var(--blue));
    transform: rotate(-1deg);
    padding: 10px 0 0 20px;
    color: var(--white); font: 800 27px/37px "Baloo 2", sans-serif;
    z-index: 2;
  }

  .slogan {
    position: absolute; left: 40px; top: 690px; width: 460px;
    text-align: center; color: var(--gold-text);
    font: 900 22px/25px "Montserrat", sans-serif; text-transform: uppercase;
    transform: rotate(-2deg);
  }
  .net-weight {
    position: absolute; left: 0; top: 762px; width: 540px; text-align: center;
    color: var(--gold-text); font: 800 12px "Montserrat", sans-serif;
  }
</style>
</head>
<body>
  <div class="pouch">
    <svg class="pouch-art" viewBox="0 0 540 800">
      <defs>
        <radialGradient id="jerkyTone" cx="0.55" cy="0.45" r="0.7">
          <stop offset="0" stop-color="var(--photo-mid)"/>
          <stop offset="1" stop-color="var(--photo-dark)"/>
        </radialGradient>
      </defs>
      <g class="seal-lines" stroke="#ffc24d" stroke-width="1.2" opacity="0.8">
        <line x1="0" y1="22" x2="540" y2="22"/><line x1="0" y1="28" x2="540" y2="28"/>
        <line x1="0" y1="34" x2="540" y2="34"/><line x1="0" y1="50" x2="540" y2="50"/>
        <line x1="0" y1="56" x2="540" y2="56"/><line x1="0" y1="62" x2="540" y2="62"/>
      </g>
      <rect class="hang-hole" x="220" y="32" width="100" height="24" rx="10" fill="var(--white)"/>
      <path class="header-sheen" d="M36,110 L504,110 L504,320 C430,355 400,360 340,395 C270,430 170,420 40,368 Z" fill="var(--silver)"/>
      <path class="header-panel" d="M36,110 Q36,80 68,80 L472,80 Q504,80 504,110 L504,290 C430,325 395,330 335,365 C268,400 170,392 40,335 Z" fill="var(--ink)"/>
      <path class="product-window" role="img" aria-label="Window showing dark glazed mushroom jerky pieces"
            d="M190,470 C230,420 320,420 360,432 C420,430 470,420 504,415 L504,660 C450,690 370,705 300,705 C230,705 170,680 160,600 C152,540 165,500 190,470 Z"
            fill="url(#jerkyTone)"/>
    </svg>

    <div class="plant-badge"><span class="dot"></span>Plant-Based</div>

    <h1 class="product-title">
      <span class="line-1">MUSHROOM</span>
      <span class="line-2">– JERKY –</span>
    </h1>

    <div class="brand-tag">
      <span class="mark"></span>
      <span class="name">Verdant Crest Foods</span>
    </div>

    <div class="chant">Bite it!<br>Rip it!<br>Tear it!<br>Chew it!</div>

    <p class="slogan">There is nothing meatier!<br>Not even meat!</p>
    <p class="net-weight">NET WT. 2.2 OZ (62G)</p>
  </div>
</body>
</html>
```